Opening Specials Flyer for toothNest Kelvin Park

We require a flyer design for our promotions/special offers for our new opening of Dental Practice. Please make one page flyer with designs on front and back
Opening Specials must be eye catchy, with images
FRONT - OPENING SPECIALS
BACK - MAP and Introduce our NEW CLINIC
on Back - MUST SAY "FLIP BACK OF FLYER TO VIEW OPENING SPECIAL OFFERS"

Opening specials to our local residents of Kelvin Park

Colour Scheme: Green, grey, white
Celebrate the opening of our new clinic
Opening Specials for Kelvin Park Residents include:

1. NO GAP Checkup for the whole family
NO GAP - Checkup Clean Fluoride X-rays - (to eligible health fund members)
2. Dental Crowns at half price - Full Ceramic $900 (includes core and crown, root canal extra) (please use picture of ceramic crown attached) - must bring voucher/flyer
3. Power tooth Whitening (Varden Glint)- $400 must bring voucher/flyer
1hr office in chair whitening, immediate whitening results
4. 20% off all General Dental Treatment (must bring flyer- please design this onto flyer)
5. Free Carewell Dental for Kids (for those eligible under Junior oral support Program up to $1000) - please have carewell logo
6. Free consultation for second opinion of treatment plans

Emergency dental care available after hours, please contact (02) 7356 2297

Offer valid until 31st May 2016
by appointment only
No Gap for eligible health fund members only
Address: Shop 5/12-14 Calloway Rd Kelvin Park 2290
Please have image of google map of this location

Behind the flyer (back) I would like to introduce our new clinic:
MUST INCLUDE - Flip behind for opening special offers!

toothNest Kelvin Park is your Local Family Dentist
Newly opened in March 2016, we aim to provide local residents with affordable dentistry with a gentle friendly approach. We are a child friendly practice and welcome you and your family to visit our new clinic.

www.toothnestkelvinpark.com.au
info@toothnestkelvinpark.com.au
(02) 7356 2297

Target Market(s)

Residents of Kelvin Park and Surrounding Suburbs
Children and Family

Industry/Entity Type

Dental Clinic

Colors
acd036
b2b2b2

Requirements
Must have
• (You may phrase as you please)
• Newly Opened Dental Clinic in Kelvin Park
• Special Offers until 31st May 2016
• Specials and clearly big font "NO GAP"
• Carewell logo (colour) next to "Free Carewell Dental for Kids
• MUST have toothNest Kelvin Park Logo
• Must inform that voucher must be brought in order to claim specials
• Must have address: Shop 5/12-14 Calloway Rd Kelvin Park 2290
• Must have Ph: (02) 7356 2297
Nice to have
• Image of dental crown - full ceramic (attached)
• Image of Varden Glint Whitening
• Map of Shop 5/12-14 Calloway Rd Kelvin Park (Google Map)
• Happy family picture

```html
<!DOCTYPE html>
<html lang="en">
<head>
<meta charset="utf-8">
<title>toothNest Kelvin Park – Opening Specials Flyer</title>
<link href="https://fonts.googleapis.com/css2?family=Roboto:ital,wght@0,400;0,500;0,700;0,900;1,400;1,500&family=Oswald:wght@600;700&family=Lobster&display=swap" rel="stylesheet">
<style>
  :root{
    --green:#8dc63f;
    --green-dark:#6fa52a;
    --grey:#b2b2b2;
    --grey-dark:#555659;
    --charcoal:#4a4a4a;
    --stage:#4b4b4b;
    --white:#ffffff;
    --red:#e0262c;
    --blue:#1f8fd6;
    --text:#222;
  }
  *{box-sizing:border-box;margin:0;padding:0}
  html,body{width:1200px;height:792px;overflow:hidden}
  body{background:var(--stage);font-family:Roboto,Arial,sans-serif;color:var(--text);position:relative}
  .page{position:absolute;top:24px;width:564px;height:730px;background:var(--white);overflow:hidden;box-shadow:0 6px 14px rgba(0,0,0,.35)}
  .page--front{left:28px}
  .page--back{left:610px}

  /* brand */
  .brand{position:absolute;display:flex;align-items:center;gap:8px;color:var(--grey-dark);font-weight:500;z-index:3}
  .brand__dot{width:16px;height:16px;border-radius:50%;background:var(--green)}
  .brand__name{font-size:27px;line-height:1}
  .brand__place{font-size:15px;letter-spacing:1.5px;line-height:1.2}

  /* front photo */
  .photo{position:absolute}
  .photo--family{left:0;top:0;width:564px;height:476px;background:linear-gradient(180deg,#ffffff 0%,#f4f8ec 16%,#c9dca5 40%,#8fb45a 70%,#6f9a3a 100%)}
  .photo--crowns{left:312px;top:536px;width:94px;height:54px;border-radius:24px;background:radial-gradient(circle at 40% 40%,#ffffff,#dcdcdc 70%,#c8c8c8)}

  /* opening badge */
  .badge{position:absolute;left:332px;top:22px;width:212px;text-align:center;z-index:3}
  .badge__celebrate{display:inline-block;background:var(--green);color:var(--white);font-family:Lobster,cursive;font-size:24px;padding:0 16px;line-height:30px}
  .badge__opening{font-family:Oswald,sans-serif;font-weight:700;color:var(--red);font-size:44px;line-height:46px;letter-spacing:1px}
  .badge__ribbon{display:inline-block;background:var(--blue);color:var(--white);font-size:10px;font-weight:500;padding:4px 14px;border-top:2px solid #16689f;border-bottom:2px solid #16689f}

  /* specials band */
  .band{position:absolute;left:0;top:428px;width:368px;height:48px;background:var(--green);clip-path:polygon(0 0,100% 0,94% 50%,100% 100%,0 100%);z-index:2}
  .band__title{position:absolute;left:36px;top:5px;font-size:18px;font-weight:700;line-height:18px;color:#1b1b1b}
  .band__edge{position:absolute;left:344px;top:428px;z-index:2}

  .stamp{position:absolute;left:410px;top:380px;width:132px;height:132px;border-radius:50%;background:var(--grey-dark);border:2px dashed var(--green);box-shadow:0 0 0 3px var(--white);display:flex;flex-direction:column;align-items:center;justify-content:center;color:var(--white);font-weight:700;text-align:center;z-index:3}
  .stamp__small{font-size:14px;line-height:15px}
  .stamp__big{font-size:18px;line-height:18px}

  /* specials list */
  .specials{position:absolute;left:40px;top:500px;width:380px;list-style:none}
  .special{position:relative;padding-left:30px;font-size:9px;line-height:12px;color:#333}
  .special__num{position:absolute;left:0;top:1px;width:20px;height:20px;border-radius:50%;background:var(--green);color:#1b1b1b;font-size:10px;font-weight:500;display:flex;align-items:center;justify-content:center}
  .special strong{font-weight:700}
  .special .lead{font-size:10.5px;font-weight:500;color:#111}
  .special .tiny{font-size:6.5px}
  .special em{font-style:italic}
  .special--1{margin-top:0}
  .special--2{margin-top:12px}
  .special--3{margin-top:12px}
  .special--4{margin-top:12px}
  .special--5{margin-top:10px;font-size:12px;line-height:13px}
  .special--5 strong{font-size:12px}

  .partner-badge{position:absolute;left:316px;top:608px;width:84px;height:28px;border-radius:4px;background:#1f4fa0}

  .voucher-box{position:absolute;left:434px;top:554px;width:104px;height:120px;background:var(--green);border:2px dashed var(--white);outline:1px solid var(--green);text-align:center;color:#111}
  .voucher-box__pct{font-family:Roboto,sans-serif;font-weight:900;font-size:38px;line-height:34px;margin-top:6px}
  .voucher-box__pct span{font-size:38px}
  .voucher-box__sub{font-size:10px;line-height:12px;margin-top:4px}
  .voucher-box__big{font-size:18px;line-height:18px}
  .voucher-box__note{font-size:4.8px;margin-top:4px}

  .bring-note{position:absolute;left:89px;top:686px;font-size:8px;color:#333}

  /* footer */
  .footer{position:absolute;left:0;bottom:0;width:564px;height:30px;background:var(--green);display:flex;align-items:center}
  .footer__address{color:var(--white);font-weight:700;font-size:14.5px;padding-left:26px;flex:1}
  .footer__phone{width:130px;height:100%;background:#6d6e70;color:var(--white);font-weight:500;font-size:16px;display:flex;align-items:center;justify-content:center}

  /* back */
  .photo--girl{left:0;top:0;width:564px;height:396px;background:linear-gradient(90deg,#fbfbfb 0%,#f1f1f1 42%,#e9c9b4 62%,#d9a98f 78%,#c8d98a 100%)}
  .flip{position:absolute;right:0;top:0;z-index:3}
  .flip__text{position:absolute;right:10px;top:10px;width:90px;text-align:right;font-weight:500;font-size:12.5px;line-height:15px;color:#111;z-index:4}
  .intro{position:absolute;left:66px;top:102px;width:340px;font-size:11.6px;line-height:14.5px;color:#222;z-index:2}
  .intro strong{font-weight:700}
  .contact{position:absolute;left:66px;top:204px;font-size:12px;line-height:14.5px;color:var(--green-dark);font-weight:500;z-index:2}
  .emergency{position:absolute;left:66px;top:387px;width:430px;height:36px;border-radius:12px;background:var(--green);border:2px dashed #333;display:flex;align-items:center;justify-content:center;font-size:12px;color:#111}
  .emergency em{font-style:italic;margin-right:4px}
  .emergency strong{font-weight:700}
  .validity{position:absolute;left:0;top:440px;width:564px;text-align:center;font-weight:700;font-size:12.5px;line-height:18px;color:#777;letter-spacing:.3px}
  .validity__green{color:var(--green)}
  .map{position:absolute;left:78px;top:510px;width:406px;height:172px;border-radius:14px;background:linear-gradient(160deg,#eceae4,#e3e0d8)}
</style>
</head>
<body>

<section class="page page--front">
  <div class="photo photo--family" role="img" aria-label="Happy family of four lying on the grass outdoors"></div>

  <div class="brand" style="left:40px;top:30px">
    <span class="brand__dot"></span>
    <div><div class="brand__name">toothNest</div><div class="brand__place">KELVIN PARK</div></div>
  </div>

  <div class="badge">
    <div class="badge__celebrate">Celebrate</div>
    <div class="badge__opening">OPENING</div>
    <div class="badge__ribbon">NEW Dental Clinic in Kelvin Park</div>
  </div>

  <div class="band"><div class="band__title">Opening Specials for Kelvin Park<br>Residents include:</div></div>
  <svg class="band__edge" width="30" height="48" viewBox="0 0 30 48"><polyline points="26,0 4,24 26,48" fill="none" stroke="#9a9a9a" stroke-width="4"/></svg>

  <div class="stamp">
    <div class="stamp__small">CELEBRATING<br>WITH SPECIAL<br>OFFERS UNTIL</div>
    <div class="stamp__big">31ST MAY<br>2016</div>
  </div>

  <ol class="specials">
    <li class="special special--1"><span class="special__num">1</span><span class="lead">NO GAP Checkup for the whole family</span><br><span class="lead">NO GAP</span> - Checkup Clean Fluoride X-rays - <span class="tiny">(to eligible health fund members)</span></li>
    <li class="special special--2"><span class="special__num">2</span>Dental Crowns at half price - <strong>Full Ceramic $900</strong><br>(includes core and crown, root canal extra)</li>
    <li class="special special--3"><span class="special__num">3</span><strong>Power tooth Whitening (Varden Glint)- $400</strong><br>1hr office in chair whitening, immediate whitening results</li>
    <li class="special special--4"><span class="special__num">4</span><em><strong>Free Carewell Dental for Kids (for those eligible under<br>Junior oral support Program up to $1000)</strong></em></li>
    <li class="special special--5"><span class="special__num">5</span><strong>FREE</strong> consultation for second opinion of<br>treatment plans</li>
  </ol>

  <div class="photo photo--crowns" role="img" aria-label="Full ceramic dental crowns"></div>
  <div class="partner-badge"></div>

  <div class="voucher-box">
    <div class="voucher-box__pct">20%<br>OFF</div>
    <div class="voucher-box__sub">all General Dental</div>
    <div class="voucher-box__big">Treatment</div>
    <div class="voucher-box__note">Bring voucher in order to claim specials</div>
  </div>

  <div class="bring-note">Bring voucher in order to claim specials</div>

  <footer class="footer">
    <div class="footer__address">Shop 5/12-14 Calloway Rd Kelvin Park 2290</div>
    <div class="footer__phone">(02) 7356 2297</div>
  </footer>
</section>

<section class="page page--back">
  <div class="photo photo--girl" role="img" aria-label="Smiling girl beside a dental model with braces"></div>

  <svg class="flip" width="140" height="100" viewBox="0 0 140 100">
    <polygon points="0,0 140,0 140,100" fill="#8dc63f"/>
    <path d="M0,0 Q40,20 60,40 Q90,60 140,100 L120,100 Q70,70 40,40 Q20,15 0,0 Z" fill="#bdbdbd"/>
  </svg>
  <div class="flip__text">Flip Back for Special offers</div>

  <div class="brand" style="left:66px;top:40px">
    <span class="brand__dot"></span>
    <div><div class="brand__name">toothNest</div><div class="brand__place">KELVIN PARK</div></div>
  </div>

  <p class="intro">toothNest Kelvin Park is your Local Family Dentist Newly opened in March 2016, we aim to provide local residents with affordable dentistry with a gentle friendly approach. We are a child friendly practice and <strong>welcome you and your family to visit our new clinic.</strong></p>

  <div class="contact">www.toothnestkelvinpark.com.au<br>info@toothnestkelvinpark.com.au<br>(02) 7356 2297</div>

  <div class="emergency"><em>Emergency dental care available after hours,</em> <strong>please contact (02) 7356 2297</strong></div>

  <div class="validity">Offer valid until 31st May 2016<br>by appointment only<br><span class="validity__green">No Gap for eligible health fund members only</span></div>

  <div class="map" role="img" aria-label="Street map showing the clinic location on Calloway Rd, Kelvin Park"></div>

  <footer class="footer">
    <div class="footer__address">Shop 5/12-14 Calloway Rd Kelvin Park 2290</div>
    <div class="footer__phone">(02) 7356 2297</div>
  </footer>
</section>

</body>
</html>
```